Business card for Bio pharmaceutical company

Hello,
We are a bio pharmaceutical contract manufacturing company in Brisbane, Australia. Can you please create a new business card design. Please go to our website for colours http://www.velocrine.com.au.
On the back can you include the cartoon mascot Tobin Wuzzle and the tagline
"A Global Biopharmaceutical Contract Development Manufacturing Company"
Target Market(s)
Biotechnology
Industry/Entity Type
Pharmaceutical
Contact Information for Business Card
Maria Hollingby
Business Development Manager
maria.hollingby@velocrine.com.au
1947 Kelmott Street Parvale Queesnland 4213 Australia
T: +61 7 3590 2481
M +61 427 516 093
F +61 7 3648 2057
www.velocrine.com.au
Look and feel

```html
<!DOCTYPE html>
<html lang="en">
<head>
<meta charset="utf-8">
<title>Velocrine – Maria Hollingby Business Card</title>
<link rel="stylesheet" href="https://fonts.googleapis.com/css2?family=Exo+2:wght@400;500;600;700&family=Montserrat:wght@600&display=swap">
<style>
  :root {
    --cyan: #1dd3e0;
    --white: #ffffff;
    --gold-light: #f7c948;
    --gold-dark: #c8730f;
    --navy: #1a4d72;
    --lime: #a6e22e;
    --mascot-top: #8eeaf4;
    --mascot-bottom: #35c3dc;
    --tagline: #1f3a8f;
  }
  * { margin: 0; padding: 0; box-sizing: border-box; }
  html, body { width: 1200px; height: 703px; overflow: hidden; background: var(--white); }
  .card {
    position: relative;
    width: 1200px;
    height: 703px;
    background: var(--white);
    font-family: "Exo 2", sans-serif;
    color: var(--white);
    overflow: hidden;
  }
  .card__panel { position: absolute; inset: 0; }
  .identity { position: absolute; left: 48px; top: 72px; }
  .identity__name {
    font-family: "Exo 2", sans-serif;
    font-weight: 700;
    font-size: 64px;
    letter-spacing: 1px;
    line-height: 1;
  }
  .identity__role {
    font-weight: 400;
    font-size: 31px;
    letter-spacing: 0.5px;
    margin-top: 14px;
  }
  .contacts { position: absolute; left: 38px; top: 259px; list-style: none; }
  .contacts__item {
    display: flex;
    align-items: center;
    height: 52px;
    font-family: "Montserrat", sans-serif;
    font-weight: 600;
    font-size: 29px;
    letter-spacing: 0.3px;
  }
  .contacts__item--small { font-family: "Exo 2", sans-serif; font-weight: 600; font-size: 28px; letter-spacing: 0.4px; }
  .contacts__item--address { font-family: "Exo 2", sans-serif; font-weight: 600; font-size: 24px; letter-spacing: 0.3px; }
  .contacts__icon { width: 40px; height: 40px; margin-right: 27px; flex: none; }
  .mascot {
    position: absolute;
    left: 795px; top: 40px;
    width: 265px; height: 465px;
    border-radius: 120px;
    background: linear-gradient(180deg, var(--mascot-top), var(--mascot-bottom));
  }
  .brand {
    position: absolute;
    left: 800px; top: 490px;
    display: flex; align-items: flex-start; gap: 8px;
  }
  .brand__name {
    font-family: "Exo 2", sans-serif;
    font-weight: 700;
    font-size: 58px;
    line-height: 1;
    color: var(--navy);
    margin-top: 32px;
  }
  .brand__mark { width: 42px; height: 42px; background: var(--lime); }
  .tagline {
    position: absolute;
    left: 762px; top: 590px;
    width: 392px; height: 66px;
    border-radius: 10px;
    background: var(--tagline);
    opacity: 0.85;
  }
</style>
</head>
<body>
<div class="card">
  <svg class="card__panel" width="1200" height="703" viewBox="0 0 1200 703" aria-hidden="true">
    <defs>
      <linearGradient id="edge-gold" x1="0" y1="0" x2="0" y2="1">
        <stop offset="0" stop-color="#c8730f"/>
        <stop offset="0.5" stop-color="#f7c948"/>
        <stop offset="1" stop-color="#c8730f"/>
      </linearGradient>
    </defs>
    <path d="M0,0 H594 Q894,351 594,703 H0 Z" fill="url(#edge-gold)"/>
    <path d="M0,0 H584 Q880,351 584,703 H0 Z" fill="#1dd3e0"/>
  </svg>

  <header class="identity">
    <h1 class="identity__name">Maria Hollingby</h1>
    <p class="identity__role">Business Development Manager</p>
  </header>

  <ul class="contacts">
    <li class="contacts__item">
      <svg class="contacts__icon" viewBox="0 0 40 40" aria-label="Telephone"><path d="M4 14 Q20 4 36 14 L33 19 L27 17 L27 13 Q20 11 13 13 L13 17 L7 19 Z" fill="#fff"/><rect x="9" y="20" width="22" height="14" rx="2" fill="#fff"/></svg>
      +617-3590-2481
    </li>
    <li class="contacts__item">
      <svg class="contacts__icon" viewBox="0 0 40 40" aria-label="Mobile"><rect x="10" y="2" width="20" height="36" rx="4" fill="#fff"/><rect x="13" y="6" width="14" height="14" fill="#1dd3e0"/></svg>
      +61 427 516 093
    </li>
    <li class="contacts__item">
      <svg class="contacts__icon" viewBox="0 0 40 40" aria-label="Fax"><rect x="3" y="12" width="34" height="16" rx="3" fill="#fff"/><rect x="10" y="4" width="20" height="9" fill="#fff"/><rect x="10" y="24" width="20" height="14" fill="#fff" stroke="#1dd3e0" stroke-width="2"/></svg>
      +61 7 3648 2057
    </li>
    <li class="contacts__item contacts__item--small">
      <svg class="contacts__icon" viewBox="0 0 40 40" aria-label="Email"><rect x="3" y="9" width="34" height="22" fill="#fff"/><path d="M3 9 L20 23 L37 9" fill="none" stroke="#1dd3e0" stroke-width="2.5"/></svg>
      maria.hollingby@velocrine.com.au
    </li>
    <li class="contacts__item contacts__item--small">
      <svg class="contacts__icon" viewBox="0 0 40 40" aria-label="Website"><circle cx="20" cy="20" r="17" fill="#fff"/><rect x="3" y="16" width="34" height="8" fill="#1dd3e0"/><text x="20" y="23" text-anchor="middle" font-size="8" font-weight="700" fill="#fff" font-family="Exo 2, sans-serif">www</text></svg>
      www.velocrine.com.au
    </li>
    <li class="contacts__item contacts__item--address">
      <svg class="contacts__icon" viewBox="0 0 40 40" aria-label="Address"><path d="M20 38 C10 26 7 20 7 15 A13 13 0 0 1 33 15 C33 20 30 26 20 38 Z" fill="#fff"/><circle cx="20" cy="15" r="5" fill="#1dd3e0"/></svg>
      1947 Kelmott Street Parvale Queesnland 4213
    </li>
  </ul>

  <div class="mascot" role="img" aria-label="Company mascot illustration"></div>

  <div class="brand">
    <span class="brand__name">Velocrine</span>
    <span class="brand__mark" aria-hidden="true"></span>
  </div>

  <div class="tagline" role="img" aria-label="Hand-lettered company tagline"></div>
</div>
</body>
</html>
```